Web site for Life Coaching Consultant

I require a website for a life coaching business. I have a Tidal Netware account which I set up last week. I will need to be able to add articles and testimonials. The design should communicate that RL Harbor Lanterns is there to help people breakdown personal barriers and that we are an advocate to help them achieve personal goals.
Updates

Reason: I have some designers just accepting my invitation to submit so to give them a few days to submit. I have been thrilled with the quality of the submissions Thank you.

Hi everyone

I am loving all your designs.  The only feedback I can get from people is that they feel that the runner makes the web page look like a personal coach rather than a life coach that helps people with relations, career, and personal road blocks.

Sorry                                   

Reason: Hi I have increased the deadline as there has been so many amazing designs and some of you have asked to fine tune your entries. I would like to take this opportunity to thank you all. It is going to be a tough decision. I have put a few more pictures on the project page hoping this will help

Hi I just wanted to thank you all for your great designs.  As I got so many good designs I have asked people to vote.  I will be in touch in the next day or 2.

Cheers

Target Market(s)

People with self esteem issues either woman or girls, people who want to goal set and need an advocate

Industry/Entity Type

Life Coaching

Colors
d2a4cc
e567a6

Requirements
Must have
• must have bio section, logo, articles page, affirmation section and testimonial page.

```html
<!DOCTYPE html>
<html lang="en">
<head>
<meta charset="utf-8">
<title>Harbor Lanterns – Life Coaching</title>
<link href="https://fonts.googleapis.com/css2?family=Open+Sans:wght@400;600;700&family=Lora:wght@400&family=Oswald:wght@500&display=swap" rel="stylesheet">
<style>
:root{
  --pink:#e2206f;
  --pink-soft:#e567a6;
  --ink:#2b2b2b;
  --grey-text:#555;
  --band:#ececec;
  --footer:#3b3b3b;
  --footer-base:#1f1f1f;
  --footer-link:#c9c9c9;
  --gold:#e9a90f;
  --olive:#9aa800;
}
*{box-sizing:border-box;margin:0;padding:0}
html,body{width:826px;height:1200px;overflow:hidden;background:#fff}
body{position:relative;font-family:Arial,Helvetica,sans-serif;color:var(--ink)}
.abs{position:absolute}

/* header */
.brand{left:76px;top:32px;display:flex;align-items:center;gap:8px}
.brand-dot{width:22px;height:22px;border-radius:50%;background:var(--pink)}
.brand-name{font-family:'Open Sans',sans-serif;font-weight:600;font-size:19px;color:var(--pink);line-height:1;white-space:nowrap}
.touch{right:74px;top:9px;display:flex;align-items:center;gap:4px;font-family:'Oswald',sans-serif;font-size:12px;font-weight:500;color:#333}
.touch .sq{width:21px;height:21px;background:#3d6db5;border-radius:3px}
.touch span.lbl{margin-right:6px;font-weight:400}
.call{right:74px;top:34px;font-family:'Oswald',sans-serif;color:#222;font-size:11px}
.call b{font-size:19px;font-weight:500}
.nav{left:386px;top:65px;display:flex;font-family:'Open Sans',sans-serif;font-size:10.5px}
.nav a{color:#333;text-decoration:none;height:25px;line-height:25px}
.nav a.home{background:var(--pink);color:#fff;width:60px;text-align:center;position:relative}
.nav a.home:after{content:"";position:absolute;left:26px;bottom:-5px;border:5px solid transparent;border-bottom:0;border-top-color:var(--pink)}
.nav a+a{margin-left:22px}

/* hero */
.hero{left:0;top:98px;width:826px;height:216px;background:var(--pink)}
.hero-photo{left:70px;top:105px;width:355px;height:203px;background:#fff;padding:5px}
.hero-photo div{width:100%;height:100%;background:linear-gradient(180deg,#5d6268 0%,#b8b3a6 60%,#2a2a2a 100%)}
.headline{left:446px;top:122px;width:290px;font-family:'Open Sans',sans-serif;font-weight:600;font-size:31px;line-height:34px;color:#fff}
.headline .l2{color:#222;padding-left:32px;display:block}
.headline .l3{text-align:right;display:block;padding-right:6px}
.start{left:600px;top:257px;width:156px;height:34px;border-radius:5px;background:linear-gradient(#555,#222);border:1px solid #111;color:#fff;font-family:'Open Sans',sans-serif;font-weight:600;font-size:19px;text-align:center;line-height:32px}

/* intro */
.intro-title{left:77px;top:344px;font-family:'Open Sans',sans-serif;font-weight:400;font-size:18.5px;color:#222;white-space:nowrap}
.intro-title em{font-style:normal;color:var(--pink)}
.intro-copy{left:80px;top:379px;width:390px;font-size:8.6px;line-height:11px;color:var(--grey-text)}
.intro-copy p+p{margin-top:9px}
.video{left:501px;top:335px;width:251px;height:184px;border:1px solid #ccc;background:#fff;padding:4px;box-shadow:0 0 3px rgba(0,0,0,.15)}
.video-area{width:100%;height:160px;background:linear-gradient(#e3e1da,#cfcbc0);position:relative}
.play{position:absolute;left:98px;top:56px;width:46px;height:46px;border-radius:50%;background:rgba(255,255,255,.7);border:3px solid #333}
.play:after{content:"";position:absolute;left:15px;top:10px;border:10px solid transparent;border-right:0;border-left:16px solid #222}
.video-bar{display:flex;align-items:center;gap:6px;height:14px;font-size:6px;color:#333;padding-top:3px}
.video-bar .track{flex:1;height:2px;background:#ccc;position:relative}
.video-bar .track i{position:absolute;left:0;top:0;width:75%;height:2px;background:#333}

/* features */
.features{left:0;top:530px;width:826px;height:214px;background:linear-gradient(#f1f1f1,#e6e6e6);border-top:1px solid #ddd}
.feature{width:220px}
.feature .icon{position:absolute;left:0;top:0;width:40px;height:40px;border-radius:50%;background:var(--pink)}
.feature .icon svg{width:40px;height:40px}
.feature h3{position:absolute;left:50px;top:10px;white-space:nowrap;font-family:'Open Sans',sans-serif;font-weight:400;font-size:16.5px;color:var(--pink)}
.feature p{position:absolute;left:0;top:47px;width:160px;font-size:8.6px;line-height:11px;color:var(--grey-text)}

/* testimonial */
.signpost{left:76px;top:781px;width:181px;height:181px;border:1px solid #ddd;background:#fff;padding:3px}
.signpost div{width:100%;height:100%;background:linear-gradient(#3e78c4,#9fc1e6 60%,#e8eef5)}
.avatar{left:280px;top:803px;width:46px;height:54px;border:1px solid #bbb;padding:2px;background:#fff}
.avatar div{width:100%;height:100%;background:linear-gradient(#cfa78c,#7b5845)}
.quote-mark{left:328px;top:780px;font-family:'Lora',serif;font-size:38px;color:#ccc;line-height:1}
.quote{left:335px;top:800px;width:390px;text-align:center;font-family:'Lora',serif;font-size:14px;line-height:19px;color:#222}
.who{left:335px;top:889px;width:390px;text-align:center;font-size:9px;line-height:11px}
.who b{font-weight:400;color:var(--olive);font-size:10px;display:block}
.cta-shadow{left:100px;top:975px;width:650px;height:10px;background:radial-gradient(ellipse at center,rgba(0,0,0,.12),rgba(0,0,0,0) 70%)}
.cta{left:333px;top:951px;width:180px;height:57px;border-radius:3px;background:linear-gradient(#f3bb2b,var(--gold) 55%,#d49300);border:1px solid #c98f00;text-align:center;color:#fff;box-shadow:0 3px 5px rgba(0,0,0,.2)}
.cta small{display:block;font-size:8.5px;padding-top:10px}
.cta strong{display:block;font-family:'Oswald',sans-serif;font-weight:500;font-size:19px;padding-top:4px;letter-spacing:.3px}

/* footer */
.footer{left:0;top:1036px;width:826px;height:142px;background:var(--footer)}
.footer-base{left:0;top:1178px;width:826px;height:22px;background:var(--footer-base);color:#999;font-size:8.3px;text-align:center;line-height:22px}
.fcol h4{font-size:12.5px;font-weight:700;color:#fff;margin-bottom:11px;white-space:nowrap}
.fcol ul{list-style:none}
.fcol li{font-size:8.6px;color:var(--footer-link);line-height:13.8px;white-space:nowrap}
.fcol h5{font-size:9.5px;color:#fff;font-weight:700;margin-bottom:6px;white-space:nowrap}
.fcol .addr li{padding-left:1px}
.ico{display:inline-block;width:9px;height:9px;vertical-align:-1px;margin-right:5px}
.social li{display:flex;align-items:center;gap:10px;height:25px;line-height:25px}
.social .dot{width:19px;height:19px;border-radius:50%;border:2px solid #fff;background:#2c6fb0}
</style>
</head>
<body>

<header>
  <div class="abs brand"><span class="brand-dot"></span><span class="brand-name">Harbor Lanterns</span></div>
  <div class="abs touch"><span class="lbl">STAY IN TOUCH</span><span class="sq"></span><span class="sq" style="background:#47a9e0"></span><span class="sq" style="background:#2f7dbb"></span></div>
  <div class="abs call">CALL US: <b>0491 508 216</b></div>
  <nav class="abs nav">
    <a class="home" href="#">Home</a><a href="#">About Us</a><a href="#" style="margin-left:44px">Services</a><a href="#" style="margin-left:44px">Traning</a><a href="#" style="margin-left:44px">Contact</a>
  </nav>
</header>

<section class="abs hero"></section>
<div class="abs hero-photo"><div role="img" aria-label="Photo of a woman standing confidently against a bright sky with an affirmation about being stronger than any excuse"></div></div>
<h1 class="abs headline">Create the life <span class="l2">you want to live</span><span class="l3">Yourself</span></h1>
<div class="abs start">Start Now</div>

<h2 class="abs intro-title">Get inspired by our <em>Life Coaching</em> websites</h2>
<div class="abs intro-copy">
  <p>images of 24 countries from 6 continents, created by Ellis Varden and Tomas Reyle, with music from Owen Halloway and others. The film has no plot, contains no actors and has no script. Instead, high quality 70mm images show some of the best, and worse, parts of nature and human life. Timelapse is used heavily to show everyday life from a different perspective. Solenne is often considered a spiritual film.</p>
  <p>Solenne is an ancient word, which can be translated as "a blessing, or as the breath, or essence of life from which the evolutionary process unfolds." For many people Solenne is the definitive film in this style.</p>
</div>
<div class="abs video">
  <div class="video-area" role="img" aria-label="Video still of hand lettered words: dream big, set goals, take action"><div class="play"></div></div>
  <div class="video-bar"><span>▶</span><span class="track"><i></i></span><span>1:23 / 2:10</span><span>◀)</span><span>□</span></div>
</div>

<section class="abs features"></section>
<svg class="abs" style="left:398px;top:742px" width="30" height="16" viewBox="0 0 30 16"><path d="M0 0 Q15 0 15 15 Q15 0 30 0 Z" fill="#e6e6e6"/></svg>

<div class="abs feature" style="left:76px;top:543px">
  <div class="icon"><svg viewBox="0 0 40 40"><path d="M23 8 L13 22 H19 L16 32 L27 17 H21 Z" fill="#fff"/></svg></div>
  <h3>Powerfull</h3>
  <p>One of the most incredible life experi-ences you will ever have that rocks you at your core.</p>
</div>
<div class="abs feature" style="left:341px;top:542px">
  <div class="icon"><svg viewBox="0 0 40 40"><circle cx="23" cy="11" r="3" fill="#fff"/><path d="M9 16 H31 M20 16 L18 24 L12 31 M18 24 L26 30" stroke="#fff" stroke-width="3" fill="none" stroke-linecap="round"/></svg></div>
  <h3>Breakthrough</h3>
  <p>Smash through the barriers that stand in the way of achieving what it is you truly desire.</p>
</div>
<div class="abs feature" style="left:576px;top:542px">
  <div class="icon"><svg viewBox="0 0 40 40"><rect x="11" y="12" width="18" height="17" rx="2" fill="#fff"/><circle cx="20" cy="14" r="4" fill="#e2206f" stroke="#fff" stroke-width="2"/></svg></div>
  <h3>Transformational</h3>
  <p>Discover your purpose in life and step into the truth of who you were meant to be.</p>
</div>
<div class="abs feature" style="left:76px;top:643px">
  <div class="icon"><svg viewBox="0 0 40 40"><path d="M14 24 H26 L24 31 H16 Z" fill="#fff"/><path d="M20 24 V15 M20 18 Q13 16 14 10 Q20 11 20 18 M20 18 Q27 16 26 10 Q20 11 20 18" stroke="#fff" stroke-width="2" fill="none"/></svg></div>
  <h3>Life Changing</h3>
  <p>Let go of the things that no longer serve you and adopt the empowering things that do.</p>
</div>
<div class="abs feature" style="left:342px;top:643px">
  <div class="icon"><svg viewBox="0 0 40 40"><circle cx="21" cy="10" r="3" fill="#fff"/><path d="M12 18 L20 15 L26 20 M20 15 L18 24 L13 30 M18 24 L26 28" stroke="#fff" stroke-width="3" fill="none" stroke-linecap="round"/></svg></div>
  <h3>Adventure</h3>
  <p>Experience the passion, joy, and excitement you love during your amaz-ing life journey.</p>
</div>
<div class="abs feature" style="left:578px;top:643px">
  <div class="icon"><svg viewBox="0 0 40 40"><circle cx="17" cy="14" r="4" fill="#fff"/><path d="M9 29 Q9 20 17 20 Q25 20 25 29 Z" fill="#fff"/><circle cx="25" cy="16" r="3" fill="#fff"/><path d="M23 22 Q31 21 31 28 H27" fill="#fff"/></svg></div>
  <h3>Free Consulation</h3>
  <p>Learn how The Bright Path Program can help you make next year the best year of your life.</p>
</div>

<div class="abs signpost"><div role="img" aria-label="Photo of a signpost against a blue sky with arrows reading who, what, where, when, why, how, questions and answers"></div></div>
<div class="abs avatar"><div role="img" aria-label="Portrait photo of the client giving the testimonial"></div></div>
<div class="abs quote-mark">“</div>
<blockquote class="abs quote">Rowan pushed me to realize my true potential and led me in the direction of success.&nbsp; I was in a "rut" when I started working with Rowan...now, I am truly on top of the world.&nbsp; Thank you Rowan, I am grateful for you!</blockquote>
<div class="abs who"><b>MIRA T.</b>Seattle, Washington</div>
<div class="abs cta-shadow"></div>
<div class="abs cta"><small>Receive a FREE Breakthrough Session</small><strong>SIGN UP NOW ▸▸</strong></div>

<footer class="abs footer"></footer>
<div class="abs fcol" style="left:77px;top:1051px">
  <h4>Quick Links</h4>
  <ul><li>Blog</li><li>About</li><li>Consulting</li><li>Coaching</li><li>Speaking</li><li>News</li><li>FAQ</li></ul>
</div>
<div class="abs fcol" style="left:214px;top:1051px">
  <h4>About us</h4>
  <ul><li>Who we are</li><li>In the press</li><li>Partners</li><li>Careers we're hiring!</li><li>Terms of service</li><li>Privacy policy</li></ul>
</div>
<div class="abs fcol" style="left:353px;top:1051px">
  <h4>Contact Us</h4>
  <h5>Harbor Lanterns Company</h5>
  <ul class="addr"><li>Three Harbor Plaza</li><li>418 Mariner Avenue, Suite 210</li><li>Tacoma, Washington 98402</li>
    <li><svg class="ico" viewBox="0 0 10 10"><path d="M2 1 L4 1 L5 3 L4 4 Q5 6 6 6 L7 5 L9 6 L9 8 Q5 9 1 3 Z" fill="#fff"/></svg>253.410.3300</li>
    <li><svg class="ico" viewBox="0 0 10 10"><rect x="2" y="1" width="6" height="3" fill="#fff"/><rect x="1" y="4" width="8" height="4" fill="#fff"/><rect x="3" y="6" width="4" height="3" fill="#3b3b3b" stroke="#fff"/></svg>253.410.3301</li></ul>
</div>
<div class="abs fcol" style="left:490px;top:1074px">
  <h5>Harbor Lanterns Company</h5>
  <ul class="addr" style="padding-left:3px"><li>2270 Cedar Lane</li><li>Fresno, California 93721</li>
    <li><svg class="ico" viewBox="0 0 10 10"><path d="M2 1 L4 1 L5 3 L4 4 Q5 6 6 6 L7 5 L9 6 L9 8 Q5 9 1 3 Z" fill="#fff"/></svg>559.240.6100</li>
    <li><svg class="ico" viewBox="0 0 10 10"><rect x="2" y="1" width="6" height="3" fill="#fff"/><rect x="1" y="4" width="8" height="4" fill="#fff"/><rect x="3" y="6" width="4" height="3" fill="#3b3b3b" stroke="#fff"/></svg>559.240.6101</li></ul>
</div>
<div class="abs fcol" style="left:669px;top:1051px">
  <h4 style="margin-bottom:5px">Follow Us On</h4>
  <ul class="social"><li><span class="dot"></span>Network</li><li><span class="dot" style="background:#3a5a98"></span>Community</li><li><span class="dot" style="background:#f08a18"></span>Blog</li><li><span class="dot" style="background:#34a7e0"></span>Updates</li></ul>
</div>
<div class="abs footer-base">2014 © harbor lanterns. ALL Rights Reserved. Privacy Policy | Terms of Service</div>

</body>
</html>
```